依頼概要
ハガキを送る際に住所と会社名、似顔絵などをいれたスタンプの作成をお願いしたいと思います。
名刺交換をした方やお世話になっている方にお礼状を書く際に、今まで住所を手書きで書いていたのですが、量が増えると大変なので、スタンプを作成したいと思います。
しかし、ただのスタンプだと味気ないので、似顔絵入りを作成したいと思います。

サイズは、30×80mm(横×縦)
https://www.morinoki-insho.example/item/kaku_030x080.html
上記のサイトから注文したいと思います。

1、住所
2、会社名
3、代表取締役と名前
この3点と顔のイラストが入った物を組み合わせていただければと思います。
身体は、スーツっぽくしてください。
これらの情報は、お願いする人が決定したらお送りします。

2名分お願いします。もう一人は、役職なしです。
納入方法は、
PDFとAiでお願いします。
宜しくお願いいたします。

色々なタイプの提案がありましたし、自分が望んだような素敵なのがあったため。

これだけ沢山の方に提案していただき、ありがとうございました。
良い意味で沢山迷いました。
また何かあった時は、宜しくお願いいたします。

```html
<!DOCTYPE html>
<html lang="ja">
<head>
<meta charset="utf-8">
<title>住所スタンプ 30×80mm</title>
<link rel="stylesheet" href="https://fonts.googleapis.com/css2?family=Noto+Sans+JP:wght@400;500;700&display=swap">
<style>
  :root {
    --ink: #111111;
    --paper: #ffffff;
    --board: #ffffff;
    --label: #333333;
    --trim: #7ec8d8;
    --shadow: rgba(0, 0, 0, 0.28);
    --art-light: #d9d9d9;
    --art-dark: #8a8a8a;
  }
  html, body {
    margin: 0;
    padding: 0;
    width: 1200px;
    height: 978px;
    overflow: hidden;
    background: var(--board);
    font-family: "Noto Sans JP", sans-serif;
    color: var(--ink);
  }
  .board {
    position: relative;
    width: 1200px;
    height: 978px;
  }
  .stamp {
    position: absolute;
    width: 164px;
    height: 444px;
    background: var(--paper);
  }
  .stamp--proof {
    left: 154px;
    top: 240px;
    outline: 1px solid var(--trim);
  }
  .stamp--on-card {
    left: 26px;
    top: 367px;
  }
  .stamp__col {
    position: absolute;
    top: 12px;
    writing-mode: vertical-rl;
    text-orientation: upright;
    margin: 0;
    line-height: 1;
    white-space: nowrap;
  }
  .stamp__company {
    left: 122px;
    font-size: 22px;
    font-weight: 500;
    letter-spacing: 0.02em;
  }
  .stamp__company-name {
    font-weight: 700;
    margin-top: 10px;
    display: inline-block;
    font-size: 25px;
  }
  .stamp__address {
    font-size: 18px;
    letter-spacing: 0.02em;
  }
  .stamp__address--line1 { left: 86px; }
  .stamp__address--line2 { left: 60px; }
  .stamp__address .tcy {
    text-combine-upright: all;
  }
  .stamp__person {
    left: 20px;
  }
  .stamp__title {
    display: block;
    font-size: 13px;
    letter-spacing: 0.04em;
  }
  .stamp__name {
    display: block;
    margin-top: 14px;
    font-size: 23px;
    font-weight: 700;
    letter-spacing: 0.04em;
  }
  .stamp__bubble {
    position: absolute;
    left: 4px;
    top: 238px;
    width: 156px;
    height: 28px;
  }
  .stamp__portrait {
    position: absolute;
    left: 6px;
    top: 262px;
    width: 152px;
    height: 176px;
    border: 1.5px solid var(--ink);
    box-sizing: border-box;
    background: linear-gradient(180deg, var(--art-light) 0%, var(--art-dark) 100%);
  }
  .card-label {
    position: absolute;
    left: 502px;
    top: 48px;
    font-size: 13px;
    color: var(--label);
    margin: 0;
  }
  .postcard {
    position: absolute;
    left: 502px;
    top: 79px;
    width: 558px;
    height: 825px;
    background: var(--paper);
    box-shadow: 6px 8px 10px var(--shadow);
  }
</style>
</head>
<body>
<main class="board">

  <section class="stamp stamp--proof" aria-label="スタンプ版下">
    <p class="stamp__col stamp__company">株式会社<span class="stamp__company-name">ミナモト</span></p>
    <p class="stamp__col stamp__address stamp__address--line1">福岡県北九州市小倉南区</p>
    <p class="stamp__col stamp__address stamp__address--line2">大字青葉１２１２番<span class="tcy">24</span>号</p>
    <p class="stamp__col stamp__person"><span class="stamp__title">代表取締役</span><span class="stamp__name">森川正和</span></p>
    <svg class="stamp__bubble" viewBox="0 0 156 28" aria-hidden="true">
      <path d="M6 2 C10 14, 30 16, 70 16 L70 26 L80 16 C126 16, 148 14, 152 2" fill="none" stroke="#111" stroke-width="1.5"/>
    </svg>
    <div class="stamp__portrait" role="img" aria-label="スーツ姿の代表者の似顔絵イラスト"></div>
  </section>

  <p class="card-label">ハガキ148mm × 100mm</p>

  <section class="postcard" aria-label="ハガキへの押印イメージ">
    <div class="stamp stamp--on-card">
      <p class="stamp__col stamp__company">株式会社<span class="stamp__company-name">ミナモト</span></p>
      <p class="stamp__col stamp__address stamp__address--line1">福岡県北九州市小倉南区</p>
      <p class="stamp__col stamp__address stamp__address--line2">大字青葉１２１２番<span class="tcy">24</span>号</p>
      <p class="stamp__col stamp__person"><span class="stamp__title">代表取締役</span><span class="stamp__name">森川正和</span></p>
      <svg class="stamp__bubble" viewBox="0 0 156 28" aria-hidden="true">
        <path d="M6 2 C10 14, 30 16, 70 16 L70 26 L80 16 C126 16, 148 14, 152 2" fill="none" stroke="#111" stroke-width="1.5"/>
      </svg>
      <div class="stamp__portrait" role="img" aria-label="スーツ姿の代表者の似顔絵イラスト"></div>
    </div>
  </section>

</main>
</body>
</html>
```